Blog Banner Design Project: Harbour Lantern Guides

Looking for a new banner for my blog " Owen Pelsworth's Harbour Lantern Guides" at http://www.harbourlanternguides-demo.net - and once design agreed also want an updated album art for the podcast that goes along with the site.
For more about the blog and what it is about:
http://www.harbourlanternguides-demo.net/about
Harbour Lantern Guides is a Luxury Travel Blog And Podcast that provides inspiration, advice and tips about luxurious travel experiences, including destinations, transportation, accommodation, and journeys, that travellers can read, listen to or watch.
Objective of the new design
(1) retain the colour scheme ideally to retain the brand identity, as have been using these colours since 2005.
(2) introduce more of my personality and make it more visually and overt that it is "Owen Pelsworth's Harbour Lantern Guides", so possibly introducing my image into the blog banner so visitors are clear and more aware of the person behind the brand.
(3) needs to have an up-market, luxury but modern feel.
(4) if possible reflect the focus on the content (destinations, transportation, accommodation, attractions and journeys) - but this maybe best left to just words as want the design to be bold and more of the branding and personality.
Ideal wording
Smallish: Owen Pelsworth's
Main wording: Harbour Lantern Guides
Sub-title/ small: luxurious destinations, transportation, accommodation and journeys.
I have a poll running with readers of my blog to rate the designs to help me to chose the final route, and so there is no need to submit any more designs. I will make the decision once the poll closes on the weekend.

```html
<!DOCTYPE html>
<html lang="en">
<head>
<meta charset="utf-8">
<title>Owen Pelsworth's Harbour Lantern Guides</title>
<link rel="stylesheet" href="https://fonts.googleapis.com/css2?family=Open+Sans:ital,wght@0,300;0,400;0,700;1,400&display=swap">
<style>
  :root {
    --page-bg: #ffffff;
    --ink: #3a3a3a;
    --ink-soft: #555555;
    --brand-purple: #8a1f9e;
    --brand-orange: #ff7a12;
    --caption-band: rgba(105, 105, 105, 0.62);
    --caption-text: #f2f2f2;
    --dot: rgba(255, 255, 255, 0.55);
    --dot-active: #ffffff;
    --button-dark: #2e2e2e;
    --field-border: #c9c9c9;
  }
  * { box-sizing: border-box; margin: 0; padding: 0; }
  html, body { width: 1200px; height: 900px; overflow: hidden; background: var(--page-bg); }
  body { position: relative; font-family: "Open Sans", Arial, sans-serif; color: var(--ink); }

  .site-banner {
    position: absolute; left: 29px; top: 49px; width: 1142px; height: 164px;
    background: linear-gradient(90deg, #b5502e 0%, #7a3a22 22%, #3f6a4a 40%, #2f7a5a 50%, #8a5bb0 68%, #e7c8ef 84%, #b05cc8 100%);
    overflow: hidden;
  }
  .banner-photo { position: absolute; inset: 0; }
  .banner-owner {
    position: absolute; left: 35px; top: 24px; height: 47px; padding: 0 14px;
    background: var(--brand-purple); color: #fff;
    font-size: 31px; font-weight: 400; line-height: 47px;
  }
  .banner-title {
    position: absolute; left: 35px; top: 74px;
    color: #fff; font-size: 50px; font-weight: 700; letter-spacing: -1.5px; line-height: 66px;
  }
  .banner-tagline {
    position: absolute; right: 24px; bottom: 10px;
    color: var(--brand-orange); font-size: 15px; font-style: italic; font-weight: 400;
  }

  .main-nav {
    position: absolute; right: 29px; top: 221px;
    display: flex; gap: 30px; list-style: none;
  }
  .main-nav a { color: var(--ink); text-decoration: none; font-size: 20px; font-weight: 400; }

  .feature-slider {
    position: absolute; left: 29px; top: 255px; width: 1142px; height: 516px; overflow: hidden;
    border: 1px solid #d6d6d6;
  }
  .feature-photo {
    position: absolute; inset: 0;
    background:
      linear-gradient(180deg, rgba(220,226,228,0.9) 0%, rgba(200,208,200,0.4) 30%, rgba(0,0,0,0) 55%),
      linear-gradient(90deg, #8a8a6a 0%, #6e6552 25%, #5e574c 50%, #6b6456 75%, #7a7660 100%);
  }
  .feature-caption {
    position: absolute; left: 0; right: 0; top: 357px; height: 159px;
    background: var(--caption-band); padding: 6px 22px 0;
  }
  .feature-title {
    color: var(--caption-text); font-size: 43px; font-weight: 300; line-height: 50px; letter-spacing: 0.2px;
  }
  .feature-category { margin-top: 10px; color: var(--caption-text); font-size: 16px; font-weight: 400; }
  .slider-dots { position: absolute; left: 925px; top: 456px; display: flex; gap: 16px; }
  .slider-dots span { width: 24px; height: 24px; border-radius: 50%; background: var(--dot); }
  .slider-dots .is-active { background: var(--dot-active); }

  .poll-heading {
    position: absolute; left: 32px; top: 816px;
    font-size: 39px; font-weight: 300; color: var(--ink); white-space: nowrap;
  }
  .site-search { position: absolute; left: 853px; top: 829px; display: flex; align-items: center; }
  .search-field {
    width: 214px; height: 30px; border: 1px solid var(--field-border);
    font-size: 11px; color: #888; line-height: 28px; padding-left: 6px;
  }
  .search-button {
    width: 86px; height: 30px; background: var(--button-dark); color: #fff;
    font-size: 15px; font-weight: 700; text-align: center; line-height: 30px;
  }
  .search-clear { margin-left: 10px; color: #777; font-size: 18px; }
</style>
</head>
<body>
  <header class="site-banner">
    <div class="banner-photo" role="img" aria-label="City buildings with a portrait of the blog's host"></div>
    <div class="banner-owner">Owen Pelsworth's</div>
    <div class="banner-title">Harbour Lantern Guides</div>
    <div class="banner-tagline">luxurious destinations, transportation, accommodation and journeys</div>
  </header>

  <ul class="main-nav">
    <li><a href="#">Home</a></li>
    <li><a href="#">About</a></li>
    <li><a href="#">Top 10s</a></li>
    <li><a href="#">Podcast</a></li>
  </ul>

  <section class="feature-slider">
    <div class="feature-photo" role="img" aria-label="Elephants standing in African bushland"></div>
    <div class="feature-caption">
      <h2 class="feature-title">Victoria Falls, Lake Kariba and Chobe: Ember Trail<br>Safaris Holidays to Africa In Luxury</h2>
      <p class="feature-category">CATEGORY: Attraction, Destinations, London, London, United Kingdom</p>
    </div>
    <div class="slider-dots">
      <span></span><span></span><span></span><span class="is-active"></span><span></span>
    </div>
  </section>

  <h2 class="poll-heading">Vote For Your Favourite New Tips For</h2>

  <form class="site-search">
    <div class="search-field">Seekwell Custom Search</div>
    <div class="search-button">Search</div>
    <span class="search-clear">×</span>
  </form>
</body>
</html>
```